Brightfield Landscape Company flyer

I need a flyer to be mailed by the Kelvar parcel bureau for the open route bulk sender (orbs) program. I would two sides full color with one side dedicated to landscape construction and the other side dedicated to lawn maintenance. Services we offer for landscaping are: design, installation, drainage correction, grading, retaining walls, patios and water features. for the lawn maintenance:weekly lawn maintenance , lawn treatments, aerating / overseeding, mulch / pine needles and trimming shrubbery. The flyer has to state my contractor license number QTVR#7159. Thanks!

Target Market(s)

Homeowners with disposable incomes

Industry/Entity Type

Landscaping

Requirements
Must have
• logo, contractor seal and number. size should be 6"x12" and conform to the kpb standards for open route bulk sending.

```html
<!DOCTYPE html>
<html lang="en">
<head>
<meta charset="utf-8">
<title>Brightfield Landscape Company – Open Route Bulk Mailer</title>
<link href="https://fonts.googleapis.com/css2?family=Open+Sans:wght@400;600;700&family=Montserrat:wght@800&display=swap" rel="stylesheet">
<style>
  :root{
    --page:#eeeeea;
    --leaf:#7fad48;
    --forest:#15493a;
    --forest-deep:#0f3a2e;
    --white:#ffffff;
    --ink:#222222;
    --rule:#9a9a9a;
  }
  *{box-sizing:border-box;margin:0;padding:0}
  html,body{width:1200px;height:1200px;overflow:hidden;background:var(--page)}
  body{position:relative;font-family:"Open Sans",Arial,sans-serif}
  .card{position:absolute;left:90px;width:1020px;height:567px;overflow:hidden;box-shadow:0 2px 8px rgba(0,0,0,.18)}
  .card--front{top:18px;background:var(--white)}
  .card--back{top:615px;background:var(--leaf)}

  /* mailing side: landscape construction */
  .front-photo{position:absolute;left:0;top:0;width:491px;height:567px;
    background:linear-gradient(180deg,#9aa0a4 0%,#d9d3c4 22%,#cfc6b4 45%,#5c7d3c 70%,#3f6a2a 100%)}
  .front-photo::after{content:"";position:absolute;inset:0;
    background:linear-gradient(180deg,rgba(0,0,0,0) 55%,rgba(0,0,0,.35) 100%)}
  .seal{position:absolute;left:48px;top:46px;width:112px;height:112px;border-radius:50%;
    background:#f2efdf;border:5px solid #2f6a3c;z-index:2}
  .license{position:absolute;left:48px;top:166px;width:112px;text-align:center;z-index:2;
    color:var(--white);font-size:13px;font-weight:700;text-shadow:0 1px 2px rgba(0,0,0,.6)}
  .front-stripe{position:absolute;left:491px;top:0;width:19px;height:567px;
    background:linear-gradient(180deg,var(--forest-deep) 0%,#3d7a3b 60%,var(--leaf) 100%)}
  .contact{position:absolute;left:44px;top:372px;color:var(--white);font-size:14px;line-height:17px;z-index:2;
    text-shadow:0 1px 2px rgba(0,0,0,.5)}
  .contact__label{font-weight:700}
  .contact__group{margin-bottom:16px}
  .contact strong{font-weight:700}
  .brand{position:absolute;left:690px;top:150px;width:300px;text-align:center;color:var(--forest)}
  .brand__dot{width:40px;height:40px;border-radius:50%;background:var(--leaf);margin:0 auto 12px}
  .brand__name{font-size:29px;font-weight:400;line-height:32px;white-space:nowrap}
  .brand__sub{font-size:15px;font-weight:400;letter-spacing:8px;margin-top:0}
  .indicia{position:absolute;left:914px;top:372px;width:64px;padding:4px 2px;background:var(--white);
    border:1px solid #e4e4e4;font-size:7.5px;line-height:9.5px;text-align:center;color:var(--ink)}
  .indicia b{font-weight:700}
  .address-box{position:absolute;left:725px;top:444px;width:255px;height:81px;border:1px solid var(--rule);
    padding:22px 26px;font-size:14px;line-height:17px;color:var(--ink)}

  /* services side: lawn maintenance */
  .back-photo{position:absolute;inset:0}
  .service{position:absolute;left:0;width:440px}
  .service__tag{display:block;width:257px;height:35px;background:var(--forest);color:var(--white);
    font-size:16px;font-weight:600;line-height:35px;padding-left:44px;border-radius:0 8px 8px 0}
  .service__text{margin:13px 0 0 44px;font-size:15px;line-height:16.5px;color:var(--white);width:420px}
  .extras{position:absolute;left:44px;top:408px;width:470px;font-size:14px;line-height:16.5px;color:var(--white)}
  .extras b{font-weight:700}
  .headline{position:absolute;right:45px;top:40px;width:520px;text-align:right;color:var(--white);
    font-size:21px;font-weight:700;line-height:24px;text-shadow:0 1px 3px rgba(0,0,0,.55)}
  .cta{position:absolute;right:45px;top:420px;text-align:right;color:var(--white);text-shadow:0 1px 3px rgba(0,0,0,.55)}
  .cta__label{font-size:25px;font-weight:700;line-height:30px}
  .cta__phone{font-family:"Montserrat",Arial,sans-serif;font-weight:800;font-size:46px;line-height:52px;letter-spacing:.5px}
</style>
</head>
<body>

<section class="card card--front" aria-label="Mailing side – landscape construction">
  <div class="front-photo" role="img" aria-label="Photo of a cream stucco home with a tiled roof, patio lounge chairs and a lawn with square stepping stones"></div>
  <div class="seal" role="img" aria-label="Registered landscape contractor seal"></div>
  <div class="license">QTVR#7159</div>
  <div class="front-stripe"></div>
  <div class="contact">
    <div class="contact__group">
      <div class="contact__label">Mailing address</div>
      <div>PO Box 4172, Linwood Springs, NC 28901</div>
    </div>
    <div class="contact__group">
      <div class="contact__label">Physical address</div>
      <div>415 Hollow Crest Lane, Marlow Glen, North Carolina 28904</div>
    </div>
    <div class="contact__group">Phone <strong>555-318-4720</strong> | Fax <strong>555-318-4726</strong></div>
    <div class="contact__label">www.brightfieldlawn.example</div>
  </div>

  <div class="brand">
    <div class="brand__dot"></div>
    <div class="brand__name">Brightfield Landscape</div>
    <div class="brand__sub">COMPANY</div>
  </div>

  <div class="indicia">PRSRT STD<br>ECRWSS<br>KPB POSTAGE<br><b>PAID</b><br>ORBS RETAIL</div>
  <div class="address-box">Local<br>Postal Customer</div>
</section>

<section class="card card--back" aria-label="Services side – lawn maintenance">
  <svg class="back-photo" width="1020" height="567" viewBox="0 0 1020 567" aria-hidden="true">
    <defs>
      <linearGradient id="poolScene" x1="0" y1="0" x2="0" y2="1">
        <stop offset="0" stop-color="#2f4a2c"/>
        <stop offset=".25" stop-color="#4d6a3c"/>
        <stop offset=".38" stop-color="#3d8fcf"/>
        <stop offset=".55" stop-color="#8d8a82"/>
        <stop offset="1" stop-color="#7d776c"/>
      </linearGradient>
    </defs>
    <path d="M510 0 C462 150 455 360 595 567 L1020 567 L1020 0 Z" fill="var(--forest-deep)"/>
    <path d="M523 0 C478 150 470 360 612 567 L1020 567 L1020 0 Z" fill="url(#poolScene)" role="img" aria-label="Photo of a backyard pool with a spa, a round stone fire pit and a lounge chair on a paver patio"/>
  </svg>

  <div class="service" style="top:45px">
    <span class="service__tag">Landscape Design/Build</span>
    <p class="service__text">Proper planning is the first step towards developing<br>a beautiful landscape. It takes time, expertise and effort<br>to create that perfect plan. The design abilities of our<br>staff are simply unmatched by our competition.</p>
  </div>
  <div class="service" style="top:172px">
    <span class="service__tag">Landscape Installation</span>
    <p class="service__text">Our Landscape Installation Division offers a complete<br>range of landscape services that we are able to<br>complete, in-house.</p>
  </div>
  <div class="service" style="top:283px">
    <span class="service__tag">Landscape Management</span>
    <p class="service__text">Our highly trained and uniformed maintenance teams<br>put their stamp of professionalism on every property we<br>maintain.</p>
  </div>
  <p class="extras"><b>Landscape construction:</b><br>Design, Installation, Drainage Correction, Grading,<br>Retaining Walls, Patios, Water Features.<br><b>Lawn maintenance:</b><br>Weekly Lawn Maintenance, Lawn Treatments,<br>Aerating / Overseeding, Mulch / Pine Needles, Shrub Trimming.</p>

  <h1 class="headline">The Area's Premier Provider of<br>Landscape Services Serving Harlow County<br>and the Surrounding areas!</h1>
  <div class="cta">
    <div class="cta__label">CONTACT US NOW!</div>
    <div class="cta__phone">555-318-4720</div>
  </div>
</section>

</body>
</html>
```